Flyer Design Project

I am opening a yoga studio called Harbourlight Yoga .Pilates. Fitness
and require a flyer that will be letterbox dropped. It will two sided - DL size.100mm × 210mm

The studio will offer Vinyasa Flow Yoga and Mat Pilates classes. We aim to enable people to lead healthier, happier lives through improved strength, flexibility and general well being that regular yoga and pilates practice offers.

We offer group classes, private and semi private sessions in yoga and pilates.

it must have the logo on it- I have uploaded the logo in two versions - not sure what will look the best.

pick up one of the colours from the logo as the background colour.

Side one:
Simple and clean with one side showing logo and address details, website and with simple intro about studio (if it fits)

Location: 1st Floor, 17 Wattlegrove Parade, Kelsmoor, 3287
phone: 0412 908316
www.harbourlightkelsmoor.com.au

OPENING OCTOBER

other side - class descriptions and intro offer for new clients
$20 for 7 days of classes
$99 for 1 month unlimited.

Class descriptions:
Vinyasa Flow yoga: A class that flows from pose to pose integrating breath, alignment, strength and power. All levels are catered for in a warm room heated to around 26 degrees. You will leave feeling inspired, empowered and energised.

Mat Pilates: A strong, challenging class integrating the key principles of pilates: concentration, control, centring, precision, flowing movement and breath. Using the core as a focus to develop these principles you will be hooked on the physical freedom you experience post workout:improved strength, flexibility and vitality that pilates offers.

Private and semi Private tuition available.

Target Market(s)

mainly women, athletic, 35-55 age, middle class, well educated

Industry/Entity Type

Fitness

Requirements
Must have
• 2 pages
the logo

Should not have
• no pics

```html
<!DOCTYPE html>
<html lang="en">
<head>
<meta charset="utf-8">
<title>Harbourlight Yoga .Pilates. Fitness — Opening October</title>
<link rel="stylesheet" href="https://fonts.googleapis.com/css2?family=Cinzel:wght@500;700&family=Arimo:wght@700&display=swap">
<style>
  :root {
    --paper: #ffffff;
    --ink-dark: #3f4348;
    --sun-yellow: #f3ec22;
    --sun-orange: #e0650f;
    --band-red: #ee1c24;
    --pool-cyan: #55f2f7;
    --text-light: #ffffff;
  }
  * { margin: 0; padding: 0; box-sizing: border-box; }
  html, body { width: 1200px; height: 2522px; overflow: hidden; background: var(--paper); }
  .flyer { position: relative; width: 1200px; height: 2522px; background: var(--paper); }

  .brand {
    position: absolute; top: 0; left: 0; width: 1200px; height: 799px;
    display: flex; flex-direction: column; align-items: center; justify-content: center; gap: 40px;
  }
  .brand-dot {
    width: 300px; height: 300px; border-radius: 50%;
    background: var(--sun-orange);
  }
  .brand-name {
    font-family: "Arimo", Arial, sans-serif; font-weight: 700;
    color: var(--ink-dark); font-size: 82px; line-height: 1.1; text-align: center;
    letter-spacing: 2px;
  }

  .info-panel {
    position: absolute; top: 799px; left: 0; width: 1200px; height: 1723px;
    background: linear-gradient(90deg, var(--sun-yellow) 0%, #ecb01b 45%, var(--sun-orange) 100%);
  }
  .contact {
    position: absolute; top: 80px; left: 0; width: 1200px; text-align: center;
    font-family: "Cinzel", "Copperplate", serif; font-weight: 500;
    color: var(--text-light); font-size: 48px; line-height: 62px; letter-spacing: 2px;
  }
  .contact p + p { margin-top: 56px; }

  .opening-band {
    position: absolute; top: 622px; left: 0; width: 1200px; height: 134px;
    background: var(--band-red);
    display: flex; align-items: center; justify-content: center;
    font-family: "Cinzel", "Copperplate", serif; font-weight: 700;
    color: var(--text-light); font-size: 78px; letter-spacing: 4px;
  }

  .intro-circle {
    position: absolute; left: 203px; top: 762px; width: 790px; height: 790px;
    border-radius: 50%; background: var(--pool-cyan);
    border: 16px solid var(--text-light);
    display: flex; align-items: center; justify-content: center;
  }
  .intro-text {
    width: 620px; text-align: center;
    font-family: "Arimo", Arial, sans-serif; font-weight: 700;
    color: var(--text-light); font-size: 46px; line-height: 63px;
  }
</style>
</head>
<body>
  <main class="flyer">
    <header class="brand">
      <div class="brand-dot" aria-hidden="true"></div>
      <h1 class="brand-name">Harbourlight Yoga<br>.Pilates. Fitness</h1>
    </header>

    <section class="info-panel">
      <div class="contact">
        <p>1st Floor<br>17 Wattlegrove Parade<br>Kelsmoor, 3287</p>
        <p>Phone: 0412 908316</p>
        <p>www.harbourlightkelsmoor.<br>com.au</p>
      </div>

      <div class="opening-band">OPENING OCTOBER</div>

      <div class="intro-circle">
        <p class="intro-text">Improve your strength, flexibility and general well being practicing Vinyasa Flow Yoga and Mat Pilates. Group classes, private and semi private sessions.</p>
      </div>
    </section>
  </main>
</body>
</html>
```